Copperleaf Motorized Shade Business Card

Hello, we've had our logo made. Now we are looking for a clean and cool looking business card. One side can just be the logo with any design elements that might look good with it. The other side will be Name, Phone Number and Email. There will not be an address on the card.

```html
<!DOCTYPE html>
<html lang="en">
<head>
<meta charset="utf-8">
<title>Copperleaf Motorized Shade Business Card</title>
<link rel="stylesheet" href="https://fonts.googleapis.com/css2?family=Roboto:wght@400;500;700;900&display=swap">
<style>
  :root {
    --backdrop: #3a3a3c;
    --card: #1f2024;
    --card-front: #1b1c20;
    --ink: #ffffff;
    --ink-soft: #e8e8ea;
    --emboss: #5b5d63;
    --sky: #1f8fdc;
    --sun: #f7b818;
    --navy: #0b3f73;
  }
  * { margin: 0; padding: 0; box-sizing: border-box; }
  html, body {
    width: 799px; height: 1200px; overflow: hidden;
    background: var(--backdrop);
    font-family: "Roboto", Arial, sans-serif;
  }
  .canvas { position: relative; width: 799px; height: 1200px; }
  .card {
    position: absolute; left: 90px; width: 620px; height: 354px;
    border-radius: 4px; overflow: hidden;
    box-shadow: 0 14px 30px rgba(0,0,0,.45);
  }
  .card--front { top: 120px; background: var(--card-front); }
  .card--back { top: 720px; background: var(--card); }

  .front-mark {
    position: absolute; left: 0; right: 0; top: 140px;
    display: flex; align-items: center; justify-content: center; gap: 14px;
  }
  .front-mark__square { width: 22px; height: 22px; background: var(--emboss); flex: none; }
  .front-mark__name {
    font-weight: 900; font-size: 34px; letter-spacing: 1px;
    color: var(--emboss); text-transform: uppercase; line-height: 1.05;
  }

  .back-mark {
    position: absolute; left: 34px; top: 96px; width: 270px;
    display: flex; align-items: flex-start; gap: 10px;
  }
  .back-mark__square { width: 18px; height: 18px; background: var(--sky); margin-top: 6px; flex: none; }
  .back-mark__name {
    font-weight: 900; font-size: 30px; color: var(--ink);
    text-transform: uppercase; line-height: 1.05;
  }

  .band { position: absolute; left: 0; top: 0; width: 620px; height: 354px; }

  .contact { position: absolute; left: 372px; top: 66px; color: var(--ink); }
  .contact__name { font-weight: 700; font-size: 24px; }
  .contact__role { font-size: 15px; color: var(--sky); margin-top: 2px; }
  .contact__list { list-style: none; margin-top: 16px; font-size: 15px; color: var(--ink-soft); }
  .contact__list li { display: flex; align-items: center; gap: 10px; height: 26px; }
  .contact__list svg { width: 13px; height: 13px; fill: var(--sky); flex: none; }

  .footer-name {
    position: absolute; right: 36px; bottom: 20px;
    font-weight: 700; font-size: 15px; color: var(--ink);
  }
</style>
</head>
<body>
<div class="canvas">
  <section class="card card--front">
    <div class="front-mark">
      <span class="front-mark__square"></span>
      <span class="front-mark__name">Copperleaf<br>Motorized Shades</span>
    </div>
  </section>

  <section class="card card--back">
    <div class="back-mark">
      <span class="back-mark__square"></span>
      <span class="back-mark__name">Copperleaf Motorized Shades</span>
    </div>

    <svg class="band" viewBox="0 0 620 354" aria-hidden="true">
      <rect x="0" y="300" width="140" height="16" fill="var(--sky)"/>
      <rect x="140" y="300" width="150" height="16" fill="var(--sun)"/>
      <path d="M280 354 L290 316 L320 316 Q330 286 360 286 H620 V354 Z" fill="var(--navy)"/>
    </svg>

    <div class="contact">
      <div class="contact__name">Ethan Marlowe</div>
      <div class="contact__role">Managing Director</div>
      <ul class="contact__list">
        <li><svg viewBox="0 0 24 24"><path d="M6.6 10.8a15.1 15.1 0 0 0 6.6 6.6l2.2-2.2a1 1 0 0 1 1-.25 11.4 11.4 0 0 0 3.6.57 1 1 0 0 1 1 1V20a1 1 0 0 1-1 1A17 17 0 0 1 3 4a1 1 0 0 1 1-1h3.5a1 1 0 0 1 1 1c0 1.25.2 2.45.57 3.57a1 1 0 0 1-.25 1z"/></svg>555-204-7731</li>
        <li><svg viewBox="0 0 24 24"><path d="M2 5h20v14H2z M2 5l10 8 10-8"/></svg>ethan@copperleafshades.com</li>
        <li><svg viewBox="0 0 24 24"><circle cx="12" cy="12" r="10"/></svg>www.copperleafshades.com</li>
      </ul>
    </div>

    <div class="footer-name">Copperleaf Motorized Shades</div>
  </section>
</div>
</body>
</html>
```